energy rating company

Web Design graphics and layout only

To create two pages for the website. First the home page and the second is the design for the job board for our clients use after login. I have attached files that explain in detail what the pages should have and the purpose/desires of each object. Please read these thoroughly.

The webpages need to be clean, professional, easy on the eye, obvious in all its buttons and functions with a strong call to action on the home page and branding and clean, great and obvious looking buttons and very simple but dynamic as well. We wish to be seen as contemporary.

Business Concept

Our business concept is simple, to build a website whereby our clients will be able to upload jobs for energy raters to quote on and subsequent complete the work if their quote is selected. To link energy ratings that are required with energy raters via our website. Similarly to the varlo website, jobs will be “advertised” on the job board and raters will select which jobs they wish to quote for.

I have attached a Word document explaining all the parts of the website and another word document showing what we are sort of after and a excel spreadsheet as well. Please read these in conjunction with this brief!
Updates

Dear All

I have submitted with my brief a word doc and excel spreadsheet of the two pages I want created.  However this is not the layout or design I want, I only put it together so that you will need to know what is required on each page.  Feel free to change and redesign it all.

Also the second page does not require the "process" logo or any other menu items except the first five being Home, How it works, About Us, testimonials and Contact us as per the home page.

We also are looking for something very professional and very clean.  It should be very easy to see exactly what you are looking for.

I will also extend the deadline for new designers!!  I am excited to see your talents!!

Thanks

I have increase budget and posted a note saying feel free to change all the details layout etc on my brief just include everything!!! 

Wanting a professional corporate look...

Want a professional corporate look

We have changed our minds and you we no longer require the process to be on the home page.

Thanks

Target Market(s)

Target Market

Home Inspection Companies
Pest Inspection Companies
Residential home buyers/sellers
Real Estate companies

Industry/Entity Type

It Company

Number of Pages Required

1 page

Requirements
Must have
• Colours and Styles

• The website should be mainly white as I believe it is seen as clean and simple with colour from the logos, but can be swayed if it projects the image we are after.

• It should be obvious and process orientated and I do believe symbols, pictures, etc should replace words where possible.

```html
<!DOCTYPE html>
<html lang="en">
<head>
<meta charset="utf-8">
<title>Voltra Australia – Energy Rating Quotes</title>
<link rel="stylesheet" href="https://fonts.googleapis.com/css2?family=Source+Sans+3:wght@400;600;700&family=Roboto:wght@400;500;700&family=Lora:ital,wght@0,400;1,400;1,700&display=swap">
<style>
:root{
  --green-top:#6cb437;
  --green-bottom:#1f9140;
  --nav:#1f7a3d;
  --nav-dark:#165f2f;
  --orange:#d98a1a;
  --orange-light:#f0b13a;
  --brand-orange:#c9661b;
  --text-green:#3f9a2b;
  --teal:#2f9a6a;
  --grey:#555;
  --grey-light:#8a8a8a;
  --callout-text:#e08a16;
  --panel:#fff;
  --table-head:#e4f4ea;
  --row-alt:#ececec;
}
*{box-sizing:border-box;margin:0;padding:0}
html,body{width:1200px;height:2257px;overflow:hidden}
body{position:relative;font-family:"Roboto",Arial,sans-serif;
  background:linear-gradient(180deg,var(--green-top) 0,var(--green-bottom) 1100px,var(--green-top) 1168px,var(--green-bottom) 2257px);}
.abs{position:absolute}
.panel{position:absolute;left:74px;width:1055px;background:var(--panel);border-radius:10px;box-shadow:0 2px 6px rgba(0,0,0,.2)}
.copyright{position:absolute;left:74px;font-size:12px;color:#b9f0a8}
.logo-box{position:absolute;left:70px;width:363px;height:137px;background:linear-gradient(#fff,#eee);border-radius:6px;box-shadow:0 2px 5px rgba(0,0,0,.25);display:flex;align-items:center;padding-left:30px;gap:16px}
.logo-dot{width:60px;height:60px;border-radius:50%;background:var(--orange-light)}
.logo-name{font-family:"Source Sans 3",sans-serif;font-weight:700;font-size:40px;color:var(--brand-orange)}
.main-nav{position:absolute;left:451px;width:656px;height:55px;background:linear-gradient(var(--nav),var(--nav-dark));border-radius:0 0 8px 8px;display:flex;align-items:center;justify-content:space-around;font-family:"Source Sans 3",sans-serif;font-size:20px;color:#fff}
.main-nav a:first-child{background:rgba(0,0,0,.15);padding:16px 12px}
.cta{position:absolute;width:205px;height:69px;border-radius:7px;background:linear-gradient(var(--orange-light),var(--orange));box-shadow:0 2px 3px rgba(0,0,0,.25);color:#fff;font-family:"Source Sans 3",sans-serif;font-size:24px;display:flex;flex-direction:column;align-items:center;justify-content:center;line-height:1.05;text-align:center}
.cta small{font-size:15px}
.process{position:absolute;left:95px;top:204px;width:1010px;height:142px;border-radius:10px;background:linear-gradient(#f0f0f0,#fff 60%,#f2f2f2)}
.step{position:absolute;width:150px;text-align:center;font-family:"Source Sans 3",sans-serif;font-size:21px;line-height:1;color:#555;transform:translateY(-50%)}
.step b{font-weight:400;color:#222}
.chev{position:absolute;top:42px}
.intro{left:104px;top:366px;width:650px;font-size:18px;font-weight:500;color:var(--text-green);line-height:26px}
.lede{left:104px;top:463px;width:650px;font-size:15.5px;color:#444;line-height:22px}
.callout{position:absolute;left:70px;top:527px;width:702px;height:159px;border-radius:6px;background:linear-gradient(#fffdf7,#fde8bf);box-shadow:0 1px 4px rgba(0,0,0,.2);padding:22px 34px;color:var(--callout-text);font-size:22px;line-height:32px}
.callout p+p{font-size:27px;margin-top:14px}
.register{left:104px;top:702px;width:660px;font-size:16.5px;font-weight:500;color:#888;line-height:22px}
.benefits{left:118px;top:768px;list-style:none;font-size:16.5px;color:#444;line-height:22px}
.benefits li{padding-left:25px;position:relative}
.benefits li::before{content:"";position:absolute;left:0;top:9px;width:6px;height:6px;border-radius:50%;background:#6fc23c}
.free{left:104px;top:939px;width:650px;font-size:17px;font-weight:500;color:#222;line-height:22px}
.login{position:absolute;left:791px;top:368px;width:341px;height:202px;border-radius:6px;background:linear-gradient(90deg,#6eaf3b,#a7c63a);padding:14px 22px;font-family:"Source Sans 3",sans-serif;color:#fff}
.login label{display:flex;align-items:center;gap:10px;font-size:22px}
.login label::before{content:"";width:8px;height:8px;border-radius:50%;background:#fff;box-shadow:0 0 0 2px #2d7a2d}
.field{height:34px;margin:6px 0 12px;background:#fff;border-radius:5px;box-shadow:inset 0 1px 3px rgba(0,0,0,.3);color:#666;font-family:"Roboto",sans-serif;font-size:16px;padding:7px 10px}
.forgot{font-family:"Roboto",sans-serif;font-size:12px;color:#eaffd0}
.testimonials{position:absolute;left:792px;top:607px;width:315px;height:428px;border-radius:10px;background:linear-gradient(#f2f2f2,#fff 30%,#fff 80%,#f2f2f2)}
.testimonials h2{position:absolute;left:12px;top:12px;font-family:"Source Sans 3",sans-serif;font-weight:400;font-size:30px;color:#2a9a5e}
.quote{position:absolute;left:10px;width:295px;font-family:"Lora",serif}
.quote p{position:absolute;left:28px;top:0;width:160px;text-align:right;font-size:14px;line-height:20px;color:#888}
.quote .photo{position:absolute;left:198px;top:0;width:88px;height:88px;border:2px solid #f0a81e;background:linear-gradient(#8a6a50,#3a2a20)}
.quote .mark{position:absolute;font-family:"Lora",serif;font-size:48px;font-weight:700;color:#8bbf3a;line-height:1}
.quote .who{position:absolute;left:18px;font-style:italic;font-size:14px;font-weight:700;color:#333}
.quote .where{position:absolute;left:18px;font-style:italic;font-size:12px;color:#555}
.welcome{position:absolute;left:95px;top:1370px;width:1005px;height:62px;border-radius:8px;background:linear-gradient(#f2f2f2,#fff)}
.welcome h1{position:absolute;left:44px;top:10px;font-weight:400;font-family:"Roboto",sans-serif;font-size:30px;color:var(--brand-orange)}
.welcome h1 span{font-size:25px}
.welcome .leaf{position:absolute;left:18px;top:24px;width:13px;height:13px;border-radius:50%;background:#5aa832}
.account-links{position:absolute;right:30px;top:22px;display:flex;gap:22px;font-size:13px;color:var(--teal);align-items:center}
.account-links span{display:flex;align-items:center;gap:6px}
.detail{position:absolute}
.detail dt{font-size:16px;color:#e08a16;font-family:"Roboto",sans-serif}
.detail dd{font-family:"Lora",serif;font-size:14px;color:#999}
.tab{position:absolute;top:1686px;height:44px;border-radius:6px 6px 0 0;background:#2c9a56;color:#fff;font-family:"Source Sans 3",sans-serif;font-size:21px;display:flex;align-items:center;justify-content:center}
.tab.on{background:#1d7a40}
.jobs-wrap{position:absolute;left:107px;top:1728px;width:987px;height:446px;border-radius:6px;background:linear-gradient(#7aaa3a,#a9c43a)}
.jobs{position:absolute;left:15px;width:955px;background:#fff;border-radius:6px;border-collapse:collapse;overflow:hidden;font-size:11px;color:#444;table-layout:fixed}
.jobs th{background:var(--table-head);color:var(--teal);font-weight:700;font-size:12px;height:59px;text-align:left;padding:0 8px;vertical-align:middle;line-height:20px}
.jobs th.c{text-align:center}
.jobs td{height:39px;padding:0 12px}
.jobs tr.alt td{background:var(--row-alt)}
.jobs td.job{background:#fff!important;color:var(--teal);font-weight:700;font-size:11.5px;padding-left:8px}
.jobs td.job span{color:#5bbf3a;font-size:18px;vertical-align:-2px;margin-right:5px}
.jobs td.ic{padding:0;text-align:center}
</style>
</head>
<body>

<!-- ===== Home page ===== -->
<div class="panel" style="top:33px;height:1070px"></div>
<div class="logo-box" style="top:40px"><span class="logo-dot"></span><span class="logo-name">Voltra Australia</span></div>
<nav class="main-nav" style="top:30px"><a>HOME</a><a>HOW IT WORKS?</a><a>ABOUT US</a><a>TESTIMONIALS</a><a>CONTACT US</a></nav>
<a class="cta" style="left:459px;top:104px">GET A QUOTE</a>
<a class="cta" style="left:676px;top:104px">ENERGY RATERS<small>Add your business</small></a>
<a class="cta" style="left:894px;top:104px">ACTIVE<br>JOB BOARD</a>

<section class="process">
  <div class="step" style="left:32px;top:73px">Post a <b>job</b></div>
  <div class="step" style="left:220px;top:70px">Get as many<br><b>quotes as<br>you like</b></div>
  <div class="step" style="left:425px;top:70px">Select energy<br><b>quote that<br>suits</b></div>
  <div class="step" style="left:631px;top:68px">Approve<br><b>payment</b></div>
  <div class="step" style="left:822px;top:70px">Receive<br><b>Rating</b></div>
  <svg class="chev" style="left:180px" width="40" height="58" viewBox="0 0 40 58"><path d="M4 2h14l20 27-20 27H4l20-27z" fill="#2e9a45"/></svg>
  <svg class="chev" style="left:383px" width="40" height="58" viewBox="0 0 40 58"><path d="M4 2h14l20 27-20 27H4l20-27z" fill="#2e9a45"/></svg>
  <svg class="chev" style="left:587px" width="40" height="58" viewBox="0 0 40 58"><path d="M4 2h14l20 27-20 27H4l20-27z" fill="#2e9a45"/></svg>
  <svg class="chev" style="left:792px" width="40" height="58" viewBox="0 0 40 58"><path d="M4 2h14l20 27-20 27H4l20-27z" fill="#2e9a45"/></svg>
</section>

<p class="abs intro">We provide you with solutions to your energy rating needs!&nbsp; Get up to 10 competitive quotes for your energy ratings from our database of professional accredited energy raters in all states and territories!</p>
<p class="abs lede">Voltra australia is Australia's leading professional energy rating consultancy firm specializing in large scaled residential and commercial energy rating logistics.</p>

<div class="callout"><p>It's Free, Fast and Easy to use and you get the best price and turnaround time that suits you!!</p><p>Its a one stop shop for your energy rating needs!!</p></div>

<p class="abs register">Register with us, upload your job and specifications, and sit back and watch as energy raters provide quotes for your work!</p>
<ul class="abs benefits">
  <li>Get up to 10 best priced quotes for your energy ratings</li>
  <li>You save time</li>
  <li>Be able to specify your desired turnaround times</li>
  <li>You can upload a job for quoting anytime and anywhere</li>
  <li>Choose a deadline for energy raters to supply quotes</li>
  <li>Be able to track your numerous jobs in one place</li>
</ul>
<p class="abs free">Its totally free to be registered with us and there is no obligations or hidden catches!</p>

<form class="login">
  <label>User</label><div class="field">mirac</div>
  <label>Password</label><div class="field" style="letter-spacing:2px">●●●●●●●●●●</div>
  <div class="forgot">Did you forget your password</div>
</form>

<aside class="testimonials">
  <h2>TESTIMONIALS</h2>
  <div class="quote" style="top:60px">
    <span class="mark" style="left:0;top:-2px">“</span>
    <p>Lorem ipsum dolor sit amet, consectetur adipiscing elit. Phasellus arcu magna, condimentum id consequat quis,</p>
    <div class="photo" role="img" aria-label="Portrait photo of client"></div>
    <div class="who" style="top:132px">Lena Marwood</div>
    <div class="where" style="top:154px">Santo Domingo, Dominican Republic</div>
    <span class="mark" style="left:254px;top:136px">”</span>
  </div>
  <div class="quote" style="top:262px">
    <span class="mark" style="left:0;top:-2px">“</span>
    <p>Lorem ipsum dolor sit amet, consectetur adipiscing elit. Phasellus arcu</p>
    <div class="photo" role="img" aria-label="Portrait photo of client" style="background:linear-gradient(#d8d8d8,#555)"></div>
    <div class="who" style="top:112px">Owen Talbert</div>
    <div class="where" style="top:133px">Arizona, United States</div>
    <span class="mark" style="left:254px;top:116px">”</span>
  </div>
</aside>
<div class="copyright" style="top:1114px">Copyright 2010 - Voltra Australia - All rights reserved</div>

<!-- ===== Job board ===== -->
<div class="panel" style="top:1200px;height:1012px"></div>
<div class="logo-box" style="top:1208px"><span class="logo-dot"></span><span class="logo-name">Voltra Australia</span></div>
<nav class="main-nav" style="top:1198px"><a>HOME</a><a>HOW IT WORKS?</a><a>ABOUT US</a><a>TESTIMONIALS</a><a>CONTACT US</a></nav>
<a class="cta" style="left:459px;top:1272px">GET A QUOTE</a>
<a class="cta" style="left:676px;top:1272px">ENERGY RATERS<small>Add your business</small></a>
<a class="cta" style="left:894px;top:1272px">ACTIVE<br>JOB BOARD</a>

<header class="welcome">
  <span class="leaf"></span>
  <h1>Welcome, <span>Mira Castell</span></h1>
  <div class="account-links">
    <span><svg width="20" height="20" viewBox="0 0 20 20"><path d="M3 17l2-6 9-9 4 4-9 9z" fill="#f0b13a"/><path d="M3 17l2-6 4 4z" fill="#e8c080"/></svg>Edit profile</span>
    <span><svg width="26" height="18" viewBox="0 0 26 18"><path d="M0 9l10-9v5h16v8H10v5z" fill="#c8262a"/></svg>Log out</span>
    <span><svg width="16" height="20" viewBox="0 0 16 20"><path d="M3 6a5 5 0 1 1 7 4c-2 1-2 2-2 4" stroke="#1e5fb0" stroke-width="3" fill="none"/><circle cx="8" cy="18" r="2" fill="#1e5fb0"/></svg>Help</span>
  </div>
</header>

<dl class="detail" style="left:118px;top:1435px"><dt>Company details</dt><dd>Toorak</dd></dl>
<dl class="detail" style="left:118px;top:1494px"><dt>E-mail address</dt><dd>Toorak</dd></dl>
<dl class="detail" style="left:118px;top:1553px"><dt>Suburb</dt><dd>Toorak</dd></dl>
<dl class="detail" style="left:118px;top:1612px"><dt>Postcode</dt><dd>3004</dd></dl>
<dl class="detail" style="left:614px;top:1435px"><dt>Contact person</dt><dd>Sam Keller</dd></dl>
<dl class="detail" style="left:614px;top:1494px"><dt>Street address</dt><dd>128 Harbour Lane</dd></dl>
<dl class="detail" style="left:614px;top:1553px"><dt>State</dt><dd>VIC</dd></dl>

<div class="tab on" style="left:114px;width:161px">QUOTING JOBS</div>
<div class="tab" style="left:283px;width:138px">ACTIVE JOBS</div>
<div class="tab" style="left:433px;width:182px">COMPLEATE JOBS</div>

<svg width="0" height="0" style="position:absolute">
  <defs>
    <symbol id="tick" viewBox="0 0 18 16"><path d="M1 9l5 5L17 2" stroke="#4aa52e" stroke-width="3.5" fill="none"/></symbol>
    <symbol id="cross" viewBox="0 0 16 16"><path d="M2 2l12 12M14 2L2 14" stroke="#c8262a" stroke-width="3.5"/></symbol>
    <symbol id="mail" viewBox="0 0 26 18"><rect x="1" y="1" width="24" height="16" fill="#f4f4f4" stroke="#bbb"/><path d="M1 1l12 9 12-9" stroke="#bbb" fill="none"/></symbol>
  </defs>
</svg>

<div class="jobs-wrap">
  <table class="jobs" style="top:16px">
    <colgroup><col style="width:120px"><col style="width:135px"><col style="width:72px"><col style="width:110px"><col style="width:115px"><col style="width:132px"><col style="width:120px"><col style="width:50px"><col style="width:50px"><col style="width:51px"></colgroup>
    <tr><th class="c">JOB</th><th>QUOTE NUMBER</th><th>PRICE</th><th>TOTAL PRICE</th><th class="c">TURNAROUND<br>TIME</th><th>REWORK PRICE</th><th>ENERGY RATERS<br>ACCREDITATION</th><th></th><th></th><th></th></tr>
    <tr class="alt"><td class="job" rowspan="3"><span>✚</span>Linden place</td><td>111111</td><td>$155,00</td><td>$180,65</td><td>1-5 days</td><td>$120,00</td><td>VIC</td><td class="ic"><svg width="16" height="14"><use href="#tick"/></svg></td><td class="ic"><svg width="15" height="15"><use href="#cross"/></svg></td><td class="ic"><svg width="24" height="17"><use href="#mail"/></svg></td></tr>
    <tr><td>111156</td><td>$250,00</td><td>$265,00</td><td>5-10 days</td><td>$150,00</td><td>QLD</td><td class="ic"><svg width="16" height="14"><use href="#tick"/></svg></td><td class="ic"><svg width="15" height="15"><use href="#cross"/></svg></td><td class="ic"><svg width="24" height="17"><use href="#mail"/></svg></td></tr>
    <tr class="alt"><td>111186</td><td>$125,00</td><td>$129,65</td><td>2 weeks</td><td>$100,00</td><td>SA</td><td class="ic"><svg width="16" height="14"><use href="#tick"/></svg></td><td class="ic"><svg width="15" height="15"><use href="#cross"/></svg></td><td class="ic"><svg width="24" height="17"><use href="#mail"/></svg></td></tr>
  </table>

  <table class="jobs" style="top:210px">
    <colgroup><col style="width:120px"><col style="width:135px"><col style="width:72px"><col style="width:110px"><col style="width:115px"><col style="width:132px"><col style="width:120px"><col style="width:50px"><col style="width:50px"><col style="width:51px"></colgroup>
    <tr><th class="c">JOB</th><th>QUOTE NUMBER</th><th>PRICE</th><th>TOTAL PRICE</th><th class="c">TURNAROUND<br>TIME</th><th>REWORK PRICE</th><th>ENERGY RATERS<br>ACCREDITATION</th><th></th><th></th><th></th></tr>
    <tr class="alt"><td class="job" rowspan="4"><span>✚</span>Linden place</td><td>111111</td><td>$155,00</td><td>$180,65</td><td>1-5 days</td><td>$120,00</td><td>VIC</td><td class="ic"><svg width="16" height="14"><use href="#tick"/></svg></td><td class="ic"><svg width="15" height="15"><use href="#cross"/></svg></td><td class="ic"><svg width="24" height="17"><use href="#mail"/></svg></td></tr>
    <tr><td>111156</td><td>$250,00</td><td>$265,00</td><td>5-10 days</td><td>$150,00</td><td>QLD</td><td class="ic"><svg width="16" height="14"><use href="#tick"/></svg></td><td class="ic"><svg width="15" height="15"><use href="#cross"/></svg></td><td class="ic"><svg width="24" height="17"><use href="#mail"/></svg></td></tr>
    <tr class="alt"><td>111186</td><td>$125,00</td><td>$129,65</td><td>2 weeks</td><td>$100,00</td><td>SA</td><td class="ic"><svg width="16" height="14"><use href="#tick"/></svg></td><td class="ic"><svg width="15" height="15"><use href="#cross"/></svg></td><td class="ic"><svg width="24" height="17"><use href="#mail"/></svg></td></tr>
    <tr><td>111313</td><td>$350,00</td><td>$354,65</td><td>Aluminum</td><td>Doors</td><td>Standard</td><td></td><td></td><td></td></tr>
  </table>
</div>

<div class="copyright" style="top:2224px">Copyright 2010 - Voltra Australia - All rights reserved</div>
</body>
</html>
```